4th Generation Family Business Needs a New Card Design!

We are a family owned 4th Generation company. We are based in the Sydney, Australia area and we are desperately in need of a more modern and classy card. We are monumental masons who design, supply & erect lasting memorials throughout cemeteries in Sydney. Our customers are normally in a period of grieving. I have attached logo files that will need to be implemented on the card. Company was established 1935. Australian Owned and Operated. Card needs to be designed to PRINTLY.com specification.

Target Market(s)

Our target market is based upon people that a grieving for family members that have passed away. We also deal with alot of companies that own and operate cemeteries.

Industry/Entity Type

Business

Contact Information for Business Card

Oliver Brantley, Operations Manager, 0417552908, oliver@hollowaystoneworks.com.au
Martin Brantley, Director, 0431906627, martin@hollowaystoneworks.com.au
Phone # 02 9634 2258
Website: www.hollowaystoneworks.com.au
Address: Suite 17, 8 Calloway Lane, East Penrose, Sydney NSW 2290

Font styles to use
Serif
Decorative
Script

Requirements
Must have
• Would like to see the logo nicely implemented with a modern design. Embossed lettering would be a nice additive.

```html
<!DOCTYPE html>
<html lang="en">
<head>
<meta charset="utf-8">
<title>Holloway Stoneworks – Business Card</title>
<link href="https://fonts.googleapis.com/css2?family=Cinzel:wght@600&family=Open+Sans:wght@400;600&display=swap" rel="stylesheet">
<style>
  :root {
    --backdrop: #3a3129;
    --card-black: #141414;
    --card-black-edge: #262626;
    --card-white: #f3f3f3;
    --gold: #e7c62a;
    --ink: #2a2a2a;
    --ink-soft: #555555;
    --rule-grey: #bdbdbd;
  }
  * { box-sizing: border-box; margin: 0; padding: 0; }
  html, body {
    width: 1200px;
    height: 1023px;
    overflow: hidden;
    background: var(--backdrop);
  }
  .canvas {
    position: relative;
    width: 1200px;
    height: 1023px;
  }
  .card {
    position: absolute;
    width: 600px;
    height: 343px;
    border-radius: 22px;
    box-shadow: 0 18px 40px rgba(0,0,0,.45);
    overflow: hidden;
  }

  /* Front */
  .card-front {
    left: 80px;
    top: 100px;
    background: radial-gradient(circle at 40% 30%, var(--card-black-edge), var(--card-black) 70%);
    display: flex;
    flex-direction: column;
    align-items: center;
    justify-content: center;
    gap: 22px;
  }
  .brand-front {
    display: flex;
    align-items: center;
    gap: 16px;
  }
  .brand-mark {
    width: 18px;
    height: 18px;
    background: var(--gold);
  }
  .brand-name {
    font-family: "Cinzel", serif;
    font-weight: 600;
    color: var(--gold);
    letter-spacing: 2px;
    line-height: 1.05;
    text-align: center;
  }
  .card-front .brand-name { font-size: 46px; }
  .front-rule {
    width: 360px;
    height: 2px;
    background: var(--rule-grey);
  }
  .website {
    font-family: "Open Sans", sans-serif;
    font-weight: 600;
    font-size: 17px;
    color: var(--gold);
    letter-spacing: .5px;
  }

  /* Back */
  .card-back {
    left: 520px;
    top: 580px;
    background: linear-gradient(135deg, #ffffff, var(--card-white) 60%, #e2e2e2);
    padding: 30px 36px;
    display: flex;
    flex-direction: column;
  }
  .brand-back {
    display: flex;
    align-items: center;
    justify-content: center;
    gap: 14px;
    height: 120px;
  }
  .card-back .brand-name {
    font-size: 34px;
    color: var(--ink);
  }
  .back-rule {
    height: 1px;
    background: var(--gold);
    margin: 12px 0 22px;
  }
  .details {
    display: flex;
    justify-content: space-between;
    align-items: flex-start;
    font-family: "Open Sans", sans-serif;
  }
  .person-name {
    font-size: 24px;
    font-weight: 600;
    color: var(--gold);
    letter-spacing: 1px;
  }
  .person-role {
    font-size: 14px;
    color: var(--ink);
    margin-top: 2px;
  }
  .contact-list {
    list-style: none;
    font-size: 13px;
    color: var(--ink);
    line-height: 1.55;
  }
  .contact-list li {
    display: flex;
    align-items: flex-start;
    gap: 8px;
  }
  .contact-list svg {
    flex: none;
    width: 13px;
    height: 13px;
    margin-top: 4px;
    fill: var(--gold);
  }
</style>
</head>
<body>
<main class="canvas">

  <section class="card card-front" aria-label="Card front">
    <div class="brand-front">
      <span class="brand-mark"></span>
      <h1 class="brand-name">HOLLOWAY<br>STONEWORKS</h1>
    </div>
    <div class="front-rule"></div>
    <p class="website">www.hollowaystoneworks.com.au</p>
  </section>

  <section class="card card-back" aria-label="Card back">
    <div class="brand-back">
      <span class="brand-mark"></span>
      <h2 class="brand-name">HOLLOWAY<br>STONEWORKS</h2>
    </div>
    <div class="back-rule"></div>
    <div class="details">
      <ul class="contact-list">
        <li>
          <svg viewBox="0 0 16 16"><path d="M4 1l3 3-2 2c1 2 3 4 5 5l2-2 3 3-2 3C7 15 1 9 1 3z"/></svg>
          0417552908
        </li>
        <li>
          <svg viewBox="0 0 16 16"><path d="M1 3h14v10H1z M2 4l6 5 6-5" stroke="#fff" stroke-width="1"/></svg>
          oliver@hollowaystoneworks.com.au
        </li>
        <li>
          <svg viewBox="0 0 16 16"><path d="M8 1a5 5 0 0 1 5 5c0 4-5 9-5 9S3 10 3 6a5 5 0 0 1 5-5zm0 3a2 2 0 1 0 0 4 2 2 0 0 0 0-4z"/></svg>
          <span>Suite 17, 8 Calloway Lane,<br>East Penrose, Sydney NSW 2290</span>
        </li>
      </ul>
      <div class="person">
        <p class="person-name">Oliver Brantley</p>
        <p class="person-role">Operations Manager</p>
      </div>
    </div>
  </section>

</main>
</body>
</html>
```